Hearthside Pots: A Patient Palate's Companion

Hi, I had a book cover designed on this site, but I want to modify the cover and change the colours. I want to keep the slow cooker and the ingredients on the cover, but I want to simplify it a bit. And, I am open to other ideas. I have attached below a book cover idea I like and I like the colors as well. I want it to be called Hearthside Pots, with the language on the right corner: "Curated For Nearly Effortless Meals That Are Greater Than The Sum Of Their Ingredients" I like the circles idea and my name as the author on the curve.

Target Market(s)

Home Cooks

Colors
00AB8E
00BBA5
67D7C9
C6EFE9
E9F9F6
F0912C
F2A743
F7CA91
FBE8D2
FDF5EE
E54698
E96AAD
F1A4CE
F9D9EA
FCEFF6
6B429C
8869AF
B7A5CE
E3DAEB
F3F0F8

Requirements
Must have
• Please use the colors on the Marigold Table Recipe Book and I like the design, but I do not want it identical. I like the author name (Harold P. Quimby) on the side of the circle on the upper right side of the cover.
Nice to have
• I like the large words "Hearthside Pots"

```html
<!DOCTYPE html>
<html lang="en">
<head>
<meta charset="utf-8">
<title>Hearthside Pots: A Patient Palate's Companion</title>
<link rel="stylesheet" href="https://fonts.googleapis.com/css2?family=DM+Serif+Display&family=Lexend:wght@300;400;700&display=swap">
<style>
  :root {
    --wood-amber: #d9970e;
    --wood-olive: #6e8a3a;
    --wood-teal: #0e8a68;
    --wood-deep: #0b7a5d;
    --circle-pink: #ff5f7e;
    --circle-red: #e23024;
    --circle-orange: #ec8020;
    --band-red: #e0312a;
    --ink: #000000;
    --paper: #ffffff;
  }
  html, body {
    margin: 0;
    padding: 0;
    width: 848px;
    height: 1200px;
    overflow: hidden;
    background: var(--paper);
  }
  .cover {
    display: block;
    width: 848px;
    height: 1200px;
  }
  .circle--pink { fill: var(--circle-pink); }
  .circle--red { fill: var(--circle-red); }
  .circle--orange { fill: var(--circle-orange); }
  .title-main {
    font-family: "DM Serif Display", Georgia, serif;
    font-size: 138px;
    fill: var(--ink);
    stroke: var(--paper);
    stroke-width: 16px;
    stroke-linejoin: round;
    paint-order: stroke fill;
  }
  .title-second {
    font-family: "Lexend", Arial, sans-serif;
    font-weight: 700;
    font-size: 120px;
    fill: var(--ink);
    stroke: var(--paper);
    stroke-width: 14px;
    stroke-linejoin: round;
    paint-order: stroke fill;
  }
  .author {
    font-family: "Lexend", Arial, sans-serif;
    font-weight: 300;
    font-size: 37px;
    letter-spacing: 1px;
    fill: var(--paper);
  }
  .subtitle {
    font-family: "Lexend", Arial, sans-serif;
    font-weight: 300;
    font-size: 48px;
    letter-spacing: 1px;
    fill: var(--paper);
  }
  .tagline-band { fill: var(--band-red); }
  .tagline {
    font-family: "Lexend", Arial, sans-serif;
    font-weight: 400;
    font-size: 24px;
    fill: var(--paper);
  }
</style>
</head>
<body>
<svg class="cover" viewBox="0 0 848 1200" xmlns="http://www.w3.org/2000/svg">
  <defs>
    <linearGradient id="woodGradient" x1="0" y1="0" x2="1" y2="0.55">
      <stop offset="0" stop-color="var(--wood-amber)"/>
      <stop offset="0.28" stop-color="var(--wood-olive)"/>
      <stop offset="0.55" stop-color="var(--wood-teal)"/>
      <stop offset="1" stop-color="var(--wood-deep)"/>
    </linearGradient>
  </defs>

  <rect class="backdrop" x="0" y="0" width="848" height="1200" fill="url(#woodGradient)" role="img" aria-label="Painted wooden planks fading from amber to teal green"/>

  <g class="circles">
    <circle class="circle--red" cx="587" cy="435" r="248"/>
    <circle class="circle--orange" cx="278" cy="629" r="248"/>
    <circle class="circle--pink" cx="299" cy="300" r="248"/>
  </g>

  <text class="author" x="807" y="68" text-anchor="end">HAROLD P. QUIMBY</text>

  <g class="title">
    <text class="title-main" x="84" y="500" textLength="680" lengthAdjust="spacingAndGlyphs">Hearthside</text>
    <text class="title-second" x="760" y="636" text-anchor="end">Pots</text>
  </g>

  <g class="subtitle-block">
    <text class="subtitle" x="830" y="833" text-anchor="end">A Patient</text>
    <text class="subtitle" x="830" y="900" text-anchor="end">Palate's</text>
    <text class="subtitle" x="830" y="963" text-anchor="end">Companion</text>
  </g>

  <rect class="tagline-band" x="0" y="1052" width="848" height="82"/>
  <text class="tagline" x="431" y="1085" text-anchor="middle">Curated For Nearly Effortless Meals That Are Greater</text>
  <text class="tagline" x="431" y="1119" text-anchor="middle">Than The Sum Of Their Ingredients</text>
</svg>
</body>
</html>
```